Statement of Qualifications Brochure for Civil/Construction Engineering Company

We need a "statement of qualification" pdf brochure with the content that is attached and in conjuncture to the new logo we are building. We also need a logo re-design (hi-rez and color) for the logo attached.

This brochure will be sent out to companies that require information of what our company does, or for requirements in services.

We would like a black and 'runway airport blue' color scheme for the brochure and the logo. It should appear professional, easy to read, and informative.
Updates

Reason: Hello, We realize our answers to some of your questions did not come to you promptly, so we have extended this deadline by 5 days. Thank you all!

Target Market(s)

Apartment Complex ownership companies. These companies typically own 10-50 mulit-unit complexes.

Industry/Entity Type

Airport

Font styles to use
Other font styles liked:
• Would like a professional, non-decorative font

Requirements
Must have
• Sharp and easy to read. Focus on information.
Nice to have
• Nice photos, we have other photos we can send to insert if necessary

```html
<!DOCTYPE html>
<html lang="en">
<head>
<meta charset="utf-8">
<title>Property Condition Assessments – Statement of Qualifications</title>
<link href="https://fonts.googleapis.com/css2?family=Questrial&family=Cabin+Condensed:wght@400;500&display=swap" rel="stylesheet">
<style>
  :root {
    --runway-blue: #2a9fd8;
    --ink: #1c1c1c;
    --grey: #5a5a5a;
    --rule: #9a9a9a;
    --paper: #ffffff;
    --earth-light: #8e6c58;
    --earth-deep: #8a4c32;
  }
  html, body { margin: 0; padding: 0; overflow: hidden; }
  body { width: 848px; height: 1200px; background: var(--paper); position: relative; font-family: "Cabin Condensed", "Arial Narrow", sans-serif; color: var(--ink); }
  .page { position: absolute; inset: 0; width: 848px; height: 1200px; overflow: hidden; }

  .running-head { position: absolute; top: 24px; right: 52px; font-family: "Questrial", Arial, sans-serif; font-size: 13px; letter-spacing: 0.3px; color: var(--runway-blue); }
  .running-head .doc-type { color: var(--grey); }
  .running-head strong { color: var(--grey); font-weight: 700; }

  .section-title { position: absolute; top: 92px; left: 51px; right: 51px; margin: 0; padding-bottom: 2px; border-bottom: 2px solid var(--rule); font-family: "Questrial", Arial, sans-serif; font-weight: 400; font-size: 31px; letter-spacing: 0.3px; color: var(--runway-blue); }

  .service-list { position: absolute; top: 149px; left: 51px; margin: 0; padding: 0; list-style: none; font-size: 14px; line-height: 21px; text-transform: uppercase; color: var(--ink); }
  .service-list li::before { content: "• "; }

  .hero-photo { position: absolute; top: 290px; left: 0; width: 848px; height: 447px; background: linear-gradient(160deg, var(--earth-light) 0%, var(--earth-deep) 100%); }

  .decor-lines { position: absolute; top: 0; left: 0; width: 848px; height: 1200px; pointer-events: none; }

  .detail-photo { position: absolute; left: 50px; width: 231px; height: 135px; }
  .detail-photo--pour { top: 771px; background: linear-gradient(160deg, #a49a8e 0%, #8f7258 100%); }
  .detail-photo--rebar { top: 917px; background: linear-gradient(150deg, #5a5048 0%, #6e5a4a 100%); }

  .body-copy { position: absolute; top: 772px; font-size: 14px; line-height: 21.2px; text-align: justify; color: var(--ink); }
  .body-copy p { margin: 0 0 21px; }
  .body-copy--left { left: 298px; width: 231px; }
  .body-copy--right { left: 546px; width: 231px; }

  .folio { position: absolute; top: 1129px; left: 51px; font-family: "Questrial", Arial, sans-serif; font-size: 13px; color: var(--grey); }
  .contact { position: absolute; top: 1129px; right: 50px; font-family: "Questrial", Arial, sans-serif; font-size: 13px; letter-spacing: 0.5px; color: var(--runway-blue); }
  .contact strong { margin-left: 10px; }
</style>
</head>
<body>
<div class="page">
  <header class="running-head">KR MERIDIAN, PLLC <span class="doc-type">• Statement of <strong>QUALIFICATIONS</strong></span></header>

  <h1 class="section-title">PROPERTY CONDITION ASSESSMENTS</h1>

  <ul class="service-list">
    <li>Conducted to ASTM E2018-08 Standards</li>
    <li>Infrastructure Condition Evaluations</li>
    <li>Building Condition and Pathology</li>
    <li>Life and Safety Assessments</li>
    <li>Seismic Risk Assessments</li>
  </ul>

  <div class="hero-photo" role="img" aria-label="Concrete highway bridge under construction on piers over red earth"></div>

  <svg class="decor-lines" viewBox="0 0 848 1200" aria-hidden="true">
    <line x1="0" y1="258" x2="152" y2="410" stroke="var(--runway-blue)" stroke-width="2"/>
    <line x1="0" y1="432" x2="257" y2="690" stroke="var(--runway-blue)" stroke-width="2"/>
    <line x1="0" y1="610" x2="174" y2="557" stroke="#ffffff" stroke-width="1.5"/>
    <line x1="0" y1="610" x2="262" y2="345" stroke="#ffffff" stroke-width="1.5"/>
    <line x1="640" y1="681" x2="848" y2="495" stroke="#ffffff" stroke-width="1.5"/>
  </svg>

  <div class="detail-photo detail-photo--pour" role="img" aria-label="Workers in hard hats and safety vests pouring a concrete wall form"></div>
  <div class="detail-photo detail-photo--rebar" role="img" aria-label="Close view of tied steel reinforcing bar cage"></div>

  <div class="body-copy body-copy--left">
    <p>ASTM E2018-08, “Property Condition Assessments: Baseline Property Condition Assessment Process” is the standard practice for most Property Condition Assessments, also referred to Property Needs Assessments. The physical condition of all components of the asset are assessed, operating documents are reviewed, agency files are accessed, and site personnel are interviewed to get the information you need.</p>
    <p>Our detailed PCA Reports describe the physical condition of the asset in easy to understand language. It includes estimated costs for the repair and replacement of items necessary to maintain asset quality.</p>
  </div>

  <div class="body-copy body-copy--right">
    <p>In addition, we provide cost estimates for capital repairs and replacements that typically cover the loan term plus two years. As with all our reports, a lot of photos are included to substantiate our findings and give our Clients a clear under- standing of everything we observed.</p>
    <p>We have evaluated thousands of commercial properties of all types. Through the years our staff has inspected apartment complexes and live/work communities, shopping centers, warehouses and manufacturing plants, low and high-rise office buildings, convenience stores and gasoline stations, and more.</p>
  </div>

  <footer>
    <span class="folio">4</span>
    <span class="contact">Midvale, TX <strong>555.018.4400</strong></span>
  </footer>
</div>
</body>
</html>
```